Bref créative
Clearwave Imaging
Business Cards, Letter Head, Envelopes
Professional
Dorothea Kessling, RDMS, RVT
President
41672 Bramblewood Ave., # 208
Santa Clarita, CA 91387
dorothea@clear-wave-im.com
www.clear-wave-im.com
Ultrasound Studies Performed:
Abdomen, Renal, Thyroid, Breast, Scrotal, GYN/OB/NT, Vascular: LE & UE Venous and Arterial, ABI, Carotid, Renal Artery, Vein Mapping, Hemodialysis Access Graft
We are launching our business card, letter head, envelopes and fax project.

```html
<!DOCTYPE html>
<html lang="en">
<head>
<meta charset="utf-8">
<title>Clearwave Imaging – Stationery</title>
<link href="https://fonts.googleapis.com/css2?family=Arimo:wght@400;700&display=swap" rel="stylesheet">
<style>
  :root {
    --backdrop: #c39a72;
    --paper: #ffffff;
    --brand-blue: #1a5fb4;
    --stripe-blue: #2a6cc4;
    --ink: #333333;
    --shadow: rgba(60, 35, 15, 0.35);
  }
  * { margin: 0; padding: 0; box-sizing: border-box; }
  html, body { width: 1200px; height: 830px; overflow: hidden; }
  body {
    position: relative;
    background: var(--backdrop);
    font-family: "Arimo", Arial, sans-serif;
    color: var(--ink);
  }
  .sheet {
    position: absolute;
    background: var(--paper);
    box-shadow: 0 3px 10px var(--shadow);
    overflow: hidden;
  }
  .corner-stripes {
    position: absolute; right: 0; bottom: 0;
    fill: var(--stripe-blue); color: var(--stripe-blue);
  }
  .brand {
    display: flex; align-items: center; gap: 8px;
    color: var(--brand-blue); font-weight: 700; line-height: 1.05;
  }
  .brand-dot { border-radius: 50%; background: var(--brand-blue); flex: none; }

  /* Letterhead */
  .letterhead { left: 31px; top: 0; width: 562px; height: 811px; }
  .letterhead .brand { position: absolute; left: 22px; top: 40px; font-size: 30px; white-space: nowrap; }
  .letterhead .brand-dot { width: 18px; height: 18px; }
  .letterhead-footer { position: absolute; left: 18px; bottom: 22px; font-size: 11px; line-height: 1.6; }
  .letterhead .corner-stripes { width: 90px; height: 90px; }

  /* Envelope */
  .envelope { left: 523px; top: 233px; width: 643px; height: 324px; }
  .envelope .brand { position: absolute; left: 34px; top: 34px; font-size: 24px; white-space: nowrap; }
  .envelope .brand-dot { width: 14px; height: 14px; }
  .envelope-return { position: absolute; left: 56px; top: 80px; font-size: 11px; line-height: 1.6; }
  .envelope .corner-stripes { width: 100px; height: 100px; }

  /* Business cards */
  .card { top: 600px; width: 255px; height: 192px; }
  .card-front { left: 595px; }
  .card-back { left: 862px; }
  .card-front .brand { position: absolute; left: 12px; top: 26px; width: 105px; font-size: 14px; gap: 6px; }
  .card-front .brand-dot { width: 9px; height: 9px; }
  .card-person { position: absolute; left: 135px; top: 28px; font-size: 8px; line-height: 1.45; }
  .card-person .person-name { color: var(--brand-blue); font-size: 9.5px; }
  .card-contact { position: absolute; left: 12px; top: 98px; font-size: 7px; line-height: 1.5; }
  .card-services { position: absolute; left: 14px; top: 24px; right: 14px; font-size: 8px; line-height: 1.5; }
  .card-services .services-heading { color: var(--brand-blue); text-transform: uppercase; }
  .card-services p + .services-heading { margin-top: 10px; }
  .card .corner-stripes { width: 46px; height: 46px; }
</style>
</head>
<body>

<svg width="0" height="0" style="position:absolute">
  <defs>
    <symbol id="stripes" viewBox="0 0 100 100">
      <polygon points="100,22 100,38 38,100 22,100"/>
      <polygon points="100,48 100,64 64,100 48,100"/>
      <polygon points="100,74 100,90 90,100 74,100"/>
    </symbol>
  </defs>
</svg>

<section class="sheet letterhead" aria-label="Letterhead">
  <div class="brand"><span class="brand-dot"></span>Clearwave Imaging</div>
  <div class="letterhead-footer">
    41672 Bramblewood Ave., # 208, Santa Clarita, CA 91387<br>
    Phone: 818-555-0172 | www.clear-wave-im.com
  </div>
  <svg class="corner-stripes" viewBox="0 0 100 100"><use href="#stripes" width="100" height="100" fill="#2a6cc4"/></svg>
</section>

<section class="sheet envelope" aria-label="Envelope">
  <div class="brand"><span class="brand-dot"></span>Clearwave Imaging</div>
  <div class="envelope-return">
    41672 Bramblewood Ave., # 208<br>
    Santa Clarita, CA 91387
  </div>
  <svg class="corner-stripes" viewBox="0 0 100 100"><use href="#stripes" width="100" height="100" fill="#2a6cc4"/></svg>
</section>

<section class="sheet card card-front" aria-label="Business card front">
  <div class="brand"><span class="brand-dot"></span><span>Clearwave Imaging</span></div>
  <div class="card-person">
    <div class="person-name">Dorothea Kessling</div>
    <div>RDMS, RVT</div>
    <div>President</div>
  </div>
  <div class="card-contact">
    41672 Bramblewood Ave., # 208<br>
    Santa Clarita, CA 91387<br>
    Phone: 818-555-0172<br>
    Email: dorothea@clear-wave-im.com<br>
    www.clear-wave-im.com
  </div>
  <svg class="corner-stripes" viewBox="0 0 100 100"><use href="#stripes" width="100" height="100" fill="#2a6cc4"/></svg>
</section>

<section class="sheet card card-back" aria-label="Business card back">
  <div class="card-services">
    <p class="services-heading">Ultrasound Studies Performed:</p>
    <p>Abdomen, Renal, Thyroid, Breast, Scrotal, GYN/OB/NT</p>
    <p class="services-heading">Vascular:</p>
    <p>LE &amp; UE Venous and Arterial, ABI, Carotid, Renal Artery, Vein Mapping, Hemodialysis Access Graft</p>
  </div>
  <svg class="corner-stripes" viewBox="0 0 100 100"><use href="#stripes" width="100" height="100" fill="#2a6cc4"/></svg>
</section>

</body>
</html>
```